Bramble Artisan Wood Fired Pizza business card design

I have a logo and need an eye catching design that will get me noticed.
My business is wood fired pizza. I want a bold design that will make our customers remember us and the food that we serve. Work with the colors of our logo and texts. Maybe add designs that lend to what or how pizza is made using our wood fired oven?

Target Market(s)

Foodies!

Contact Information for Business Card

Bramble Artisan Wood Fired Pizza
Our slogan is Fast. Fresh. Handcrafted
Catering for all events

Requirements
Must have
• Noel Pruett
Telephone 570 555 0187
website www.trybramble.com
Facebook @trybramblepizza maybe use the facebook logo next to it
Instagram trybramblepizza maybe use the instagram logo next to it
Catering for all events
Nice to have
• Maybe pizza peels, pizza cutters? Wood? Fired wood? Using our flame in the background?
Please work with different colored text so each sentence stands out? A themed color for facebook?
Maybe work with the colors within our logo?
Please try to use the our bramble font, but not a must have.

```html
<!DOCTYPE html>
<html lang="en">
<head>
<meta charset="utf-8">
<title>Bramble Artisan Wood Fired Pizza – Business Card</title>
<link rel="stylesheet" href="https://fonts.googleapis.com/css2?family=Roboto:wght@300;400&display=swap">
<style>
  :root {
    --canvas-bg: #111214;
    --card-bg: #1f1f20;
    --ink-light: #f2f2f2;
    --ink-muted: #cfcfcf;
    --flame-red: #d3141b;
    --ember-orange: #f08a1c;
    --emboss: #2d2d2e;
  }
  * { margin: 0; padding: 0; box-sizing: border-box; }
  html, body {
    width: 1200px; height: 900px; overflow: hidden;
    background: var(--canvas-bg);
    font-family: "Roboto", sans-serif;
  }
  .card {
    position: absolute;
    width: 700px; height: 400px;
    background: var(--card-bg);
    box-shadow: 0 18px 40px rgba(0,0,0,.55);
  }
  .card--front { left: 80px; top: 40px; }
  .card--back { left: 420px; top: 470px; }

  /* Front side */
  .contact-block { position: absolute; left: 60px; top: 70px; }
  .contact-name {
    color: var(--flame-red); font-size: 30px; font-weight: 400; letter-spacing: .2px;
  }
  .contact-role { color: var(--ink-muted); font-size: 18px; font-weight: 300; margin-top: 2px; }
  .divider {
    position: absolute; left: 60px; right: 40px; top: 150px;
    height: 1.5px; background: var(--ink-light);
  }
  .contact-list { position: absolute; left: 60px; top: 172px; list-style: none; }
  .contact-item {
    display: flex; align-items: center; gap: 12px;
    color: var(--ink-light); font-size: 18px; font-weight: 300; line-height: 30px;
  }
  .contact-icon { width: 16px; height: 16px; flex: none; }
  .brand-lockup {
    position: absolute; right: 50px; bottom: 70px;
    display: flex; align-items: center; gap: 12px;
  }
  .brand-dot { width: 22px; height: 22px; border-radius: 50%; background: var(--flame-red); }
  .brand-name {
    color: var(--ink-light); font-size: 42px; font-weight: 400; letter-spacing: 4px;
    text-transform: uppercase;
  }

  /* Back side */
  .brand-emboss {
    position: absolute; left: 0; right: 0; top: 120px; text-align: center;
    color: var(--emboss); font-size: 64px; font-weight: 400; letter-spacing: 8px;
    text-transform: uppercase;
  }
  .slogan {
    position: absolute; left: 0; right: 0; bottom: 60px; text-align: center;
    color: var(--ink-light); font-size: 22px; font-weight: 300; letter-spacing: 1px;
  }
  .slogan-dot { color: var(--ember-orange); margin: 0 8px; }
</style>
</head>
<body>
  <section class="card card--front" aria-label="Business card front">
    <div class="contact-block">
      <h1 class="contact-name">Noel Pruett</h1>
      <p class="contact-role">Manager</p>
    </div>
    <div class="divider"></div>
    <ul class="contact-list">
      <li class="contact-item">
        <svg class="contact-icon" viewBox="0 0 16 16" aria-hidden="true"><path d="M4 1.5l2.2 3-1.4 1.6c.9 2 2.3 3.4 4.3 4.3l1.6-1.4 3 2.2-1.2 2.6C7.5 13.6 2.4 8.5 1.4 2.7z" fill="var(--flame-red)"/></svg>
        570 555 0187
      </li>
      <li class="contact-item">
        <svg class="contact-icon" viewBox="0 0 16 16" aria-hidden="true"><g fill="none" stroke="var(--flame-red)" stroke-width="1.4"><circle cx="8" cy="8" r="6.5"/><ellipse cx="8" cy="8" rx="2.8" ry="6.5"/><path d="M1.5 8h13M2.5 4.8h11M2.5 11.2h11"/></g></svg>
        www.trybramble.com
      </li>
      <li class="contact-item">
        <svg class="contact-icon" viewBox="0 0 16 16" aria-hidden="true"><rect x="2" y="2" width="12" height="12" rx="2" fill="none" stroke="var(--flame-red)" stroke-width="1.4"/></svg>
        @trybramblepizza
      </li>
      <li class="contact-item">
        <svg class="contact-icon" viewBox="0 0 16 16" aria-hidden="true"><circle cx="8" cy="8" r="6" fill="none" stroke="var(--flame-red)" stroke-width="1.4"/></svg>
        trybramblepizza
      </li>
    </ul>
    <div class="brand-lockup">
      <span class="brand-dot"></span>
      <span class="brand-name">Bramble</span>
    </div>
  </section>

  <section class="card card--back" aria-label="Business card back">
    <p class="brand-emboss">Bramble</p>
    <p class="slogan">FAST<span class="slogan-dot">•</span>FRESH<span class="slogan-dot">•</span>HANDCRAFTED</p>
  </section>
</body>
</html>
```